http://www.lanternfieldcollective.org/

would like someone to rebuild this -http://www.lanternfieldcollective.com/ to be more modern and more easily updated

Industry/Entity Type

Non Profit

Coding

Coded - Design and coding required

Colors

Designer to choose colors to be used in the design.

Requirements
Must have
• use of the logo, and a newer design for wordpress to be hosted on Azure and easily updated templates

```html
<!DOCTYPE html>
<html lang="en">
<head>
<meta charset="utf-8">
<title>Lanternfield Collective</title>
<link rel="stylesheet" href="https://fonts.googleapis.com/css2?family=Righteous&family=Poppins:wght@400;500;600;700&family=Arimo:wght@400;700&display=swap">
<style>
:root{
  --ink:#2e2640;
  --sky:#a9cdd3;
  --ember:#e0692c;
  --rose:#e8407a;
  --white:#ffffff;
  --text:#333333;
  --muted:#777777;
  --bar:#23282d;
}
*{box-sizing:border-box;margin:0;padding:0}
html,body{width:1200px;height:3125px;overflow:hidden}
body{position:relative;background:var(--white);font-family:'Poppins',sans-serif;color:var(--text)}
.abs{position:absolute}

/* admin bar */
.admin-bar{left:157px;top:0;width:886px;height:23px;background:var(--bar);color:#ddd;font-size:9px;display:flex;align-items:center;padding:0 10px;gap:16px}
.admin-bar .right{margin-left:auto;display:flex;gap:8px;align-items:center}
.admin-bar .dot{width:10px;height:10px;border-radius:50%;background:#999;display:inline-block}

/* header */
.brand{left:0;top:40px;width:1200px;display:flex;flex-direction:column;align-items:center;gap:8px}
.brand .mark{width:64px;height:64px;border-radius:50%;background:var(--ink)}
.brand .name{font-family:'Poppins',sans-serif;font-weight:600;font-size:15px;color:var(--ink);letter-spacing:1px}
.main-nav{top:172px;left:0;width:1200px;display:flex;justify-content:center;align-items:center;font-size:10px;color:var(--ink);font-weight:500}
.main-nav a{color:inherit;text-decoration:none;margin:0 10px}
.main-nav a.current{color:var(--rose)}
.btn-give{margin-left:20px;width:89px;height:32px;border-radius:16px;background:var(--ink);color:var(--white);display:flex;align-items:center;justify-content:center}

/* frame */
.stage{left:157px;top:218px;width:886px;height:2811px;background:var(--ink);overflow:hidden}
.btn{position:absolute;display:flex;align-items:center;justify-content:center;border-radius:22px;font-size:9px;font-weight:700;letter-spacing:.3px}
.btn.sky{background:var(--sky);color:var(--white)}
.btn.light{background:var(--white);color:var(--ink)}
.title{position:absolute;font-family:'Righteous',sans-serif;font-size:27px;color:var(--white);line-height:1}
.title .accent{color:var(--sky)}
.rule{position:absolute;width:33px;height:3px;background:var(--ember)}

/* hero */
.hero-art{left:0;top:0}
.hero-quote{left:58px;top:128px;width:371px;font-family:'Arimo',sans-serif;font-size:14px;line-height:1.0;color:var(--white);text-align:justify}
.hero-head{left:456px;top:344px;font-family:'Righteous',sans-serif;font-size:28px;line-height:.92;color:var(--white)}

/* home band */
.photo-tile{position:absolute;border:3px solid var(--sky)}
.home-head{left:251px;top:536px;font-family:'Righteous',sans-serif;font-size:25px;line-height:1;color:var(--white)}

.about-text{left:508px;top:970px;width:284px;font-family:'Arimo',sans-serif;font-size:10px;font-weight:700;line-height:19px;color:var(--white);text-align:justify}

/* what we do */
.feature{position:absolute;width:240px;text-align:center;color:var(--white)}
.feature h3{font-family:'Righteous',sans-serif;font-weight:400;font-size:20px;margin-top:10px}
.feature h3 span{color:var(--sky)}
.feature p{font-size:10px;line-height:18px;margin-top:6px;height:54px}

.support-text{left:52px;top:1893px;width:360px;font-size:10px;line-height:18px;color:var(--white)}

.blog-strip{left:0;top:2200px;width:886px;height:146px;display:flex}
.blog-strip .tile{flex:1}

.map{left:45px;top:2413px;width:377px;height:331px}
.contact-label{position:absolute;font-size:11px;font-weight:600;color:var(--white)}
.contact-value{position:absolute;font-size:10px;line-height:19px;color:var(--white)}
.contact-value.dim{color:#c9c5d3;font-size:9px}
.social{position:absolute;top:2647px;left:659px;display:flex;gap:4px}
.social span{width:33px;height:33px;border-radius:50%;background:var(--sky)}

.footer-nav{left:0;top:3059px;width:1200px;display:flex;justify-content:center;gap:12px;font-size:10px;color:var(--muted)}
.copyright{left:0;top:3088px;width:1200px;text-align:center;font-size:10px;color:var(--muted)}
</style>
</head>
<body>

<div class="abs admin-bar">
  <span class="dot"></span><span>lanternfieldcollective</span><span>Customize</span><span>0</span><span>+ New</span><span>Edit Page</span><span>Edit with Pagecraft</span>
  <span class="right">Howdy, admin <span class="dot"></span></span>
</div>

<header>
  <div class="abs brand">
    <span class="mark"></span>
    <span class="name">LANTERNFIELD COLLECTIVE</span>
  </div>
  <nav class="abs main-nav">
    <a class="current">HOME</a><a>WHO WE ARE</a><a>WHAT WE DO</a><a>BLOG</a><a>CONTACT US</a><a>DONATE</a>
    <span class="btn-give">GIVE</span>
  </nav>
</header>

<main class="abs stage">
  <!-- hero -->
  <svg class="abs hero-art" width="886" height="464" role="img" aria-label="Silhouette of a mother walking with her children on a path at sunset">
    <defs>
      <linearGradient id="sunset" x1="0" y1="0" x2="0" y2="1">
        <stop offset="0" stop-color="#e57e6c"/>
        <stop offset=".55" stop-color="#f09a7c"/>
        <stop offset="1" stop-color="#3b2a2e"/>
      </linearGradient>
    </defs>
    <path d="M540 0 C440 60 470 180 420 260 C380 330 320 360 308 464 L886 464 L886 0 Z" fill="url(#sunset)"/>
  </svg>
  <p class="abs hero-quote">Then the King will say to those on His right hand, ‘Come, you blessed of My Father, inherit the kingdom prepared for you from the foundation of the world: for I was hungry and you gave Me food; I was thirsty and you gave Me drink; I was a stranger and you took Me in; I was naked and you clothed Me; I was sick and you visited Me; I was in prison and you came to Me.’ “Assuredly, I say to you, inasmuch as you did it to one of the least of these My brethren, you did it to Me.</p>
  <span class="btn sky" style="left:58px;top:292px;width:138px;height:41px">CONNECT US</span>
  <h1 class="abs hero-head">HELP NEEDY CHRISTIAN<br>WIDOWS &amp; ORPHANS</h1>
  <span class="btn sky" style="left:581px;top:411px;width:117px;height:39px">DONATE</span>

  <!-- home band -->
  <div class="photo-tile" role="img" aria-label="Mother smiling with her two young children" style="left:52px;top:538px;width:185px;height:138px;background:linear-gradient(135deg,#d9c8bf,#9e7d72)"></div>
  <h2 class="abs home-head">HELP TO<br>CREATE A<br>HOME FOR A<br>FAMILY</h2>
  <div class="photo-tile" role="img" aria-label="Small wooden house with a child standing outside" style="left:450px;top:538px;width:185px;height:138px;background:linear-gradient(180deg,#8fa9b8,#7a5a40)"></div>
  <span class="btn sky" style="left:663px;top:586px;width:171px;height:42px">GIVE YOUR SUPPORT</span>

  <!-- who we are -->
  <svg class="abs" style="left:0;top:748px" width="644" height="476" role="img" aria-label="Black and white photo of a group reading scripture together">
    <defs>
      <linearGradient id="mono" x1="0" y1="0" x2="1" y2="1">
        <stop offset="0" stop-color="#5a5a5a"/>
        <stop offset=".5" stop-color="#a8a8a8"/>
        <stop offset="1" stop-color="#3a3a3a"/>
      </linearGradient>
    </defs>
    <path d="M0 0 L644 0 C520 120 430 260 330 380 C260 450 170 476 90 476 L0 476 Z" fill="url(#mono)"/>
  </svg>
  <h2 class="title" style="left:508px;top:913px"><span class="accent">WHO</span> WE ARE</h2>
  <span class="rule" style="left:508px;top:952px"></span>
  <p class="abs about-text">Lanternfield Collective is a non-profitable organization. All donations are given to the needy families you support. The board members are 100% volunteers, (receive no salary or travel benefits). The board are members of St. Anselm Parish of Riverton and St. Brendan Parish in Fairmont. We pray that you will share with us this service to accomplish the goals of supporting these needy families in Egypt. Please pray for us, and for this service, so that God may continue to guide our work.</p>
  <span class="btn light" style="left:653px;top:1162px;width:138px;height:42px">KNOW MORE</span>

  <!-- what we do -->
  <h2 class="title" style="left:0;width:886px;text-align:center;top:1335px"><span class="accent">WHAT</span> WE DO</h2>
  <span class="rule" style="left:427px;top:1377px"></span>

  <div class="feature" style="left:57px;top:1452px">
    <svg width="100" height="76" viewBox="0 0 100 76" aria-hidden="true">
      <circle cx="45" cy="40" r="34" fill="#fff"/><circle cx="45" cy="40" r="22" fill="#a9cdd3"/><circle cx="45" cy="40" r="12" fill="#fff"/><circle cx="45" cy="40" r="6" fill="#a9cdd3"/>
      <line x1="47" y1="38" x2="96" y2="8" stroke="#fff" stroke-width="3"/>
    </svg>
    <h3><span>OUR</span> GOAL</h3>
    <p>is to feed 50 more families a day from your remnants and to add a smile to their faces.</p>
    <span class="btn light" style="left:51px;top:188px;width:138px;height:42px">KNOW MORE</span>
  </div>
  <div class="feature" style="left:323px;top:1452px">
    <svg width="100" height="76" viewBox="0 0 100 76" aria-hidden="true">
      <path d="M6 40 Q50 0 94 40 Q50 80 6 40 Z" fill="#a9cdd3"/><circle cx="50" cy="40" r="16" fill="#fff"/><circle cx="50" cy="40" r="8" fill="#a9cdd3"/>
    </svg>
    <h3><span>OUR</span> MISSION</h3>
    <p>By your support of $45 a month, you would draw smiles on the faces of widows and orphans of a needy families.</p>
    <span class="btn light" style="left:51px;top:191px;width:138px;height:42px">KNOW MORE</span>
  </div>
  <div class="feature" style="left:589px;top:1452px">
    <svg width="100" height="76" viewBox="0 0 100 76" aria-hidden="true">
      <circle cx="50" cy="36" r="18" fill="#fff"/><rect x="42" y="52" width="16" height="12" rx="3" fill="#fff"/>
      <circle cx="50" cy="36" r="6" fill="#a9cdd3"/>
      <g stroke="#fff" stroke-width="4" stroke-linecap="round"><line x1="50" y1="4" x2="50" y2="10"/><line x1="20" y1="36" x2="26" y2="36"/><line x1="74" y1="36" x2="80" y2="36"/><line x1="27" y1="14" x2="31" y2="18"/><line x1="73" y1="14" x2="69" y2="18"/><line x1="27" y1="58" x2="31" y2="54"/><line x1="73" y1="58" x2="69" y2="54"/></g>
    </svg>
    <h3><span>OUR</span> APPROACH</h3>
    <p>Lanternfield Collective is a non-profitable organization. All donations are given to the needy families you support.</p>
    <span class="btn light" style="left:51px;top:191px;width:138px;height:42px">KNOW MORE</span>
  </div>

  <!-- support -->
  <h2 class="title" style="left:52px;top:1843px"><span class="accent">SUPPORT</span> US</h2>
  <span class="rule" style="left:52px;top:1872px"></span>
  <p class="abs support-text">Support us and change the course of a child’s life today!Your donation is tax deductible.</p>
  <div class="abs" style="left:421px;top:1807px;width:269px;height:204px;background:var(--sky)"></div>
  <div class="abs" role="img" aria-label="Silhouette of a mother lifting her baby against a golden sunset over the sea" style="left:434px;top:1790px;width:275px;height:209px;background:linear-gradient(180deg,#e9a63a,#f3c250 50%,#5a3a1c)"></div>
  <span class="btn sky" style="left:722px;top:1885px;width:118px;height:41px">DONATE</span>

  <!-- blogs -->
  <h2 class="title" style="left:0;width:886px;text-align:center;top:2117px"><span class="accent">OUR</span> BLOGS</h2>
  <span class="rule" style="left:427px;top:2146px"></span>
  <div class="abs blog-strip">
    <div class="tile" role="img" aria-label="Laughing child lying in the sun" style="background:linear-gradient(135deg,#f2c46a,#e8e0d2)"></div>
    <div class="tile" role="img" aria-label="Volunteers in green shirts holding donation boxes" style="background:linear-gradient(135deg,#b54a3a,#4aa64a)"></div>
    <div class="tile" role="img" aria-label="Woman in a black dress standing in front of houses" style="background:linear-gradient(180deg,#cfd2d4,#55595a)"></div>
    <div class="tile" role="img" aria-label="Hands holding folded banknotes" style="background:linear-gradient(135deg,#7a9a5a,#d8cbb8)"></div>
  </div>
  <svg class="abs" style="left:859px;top:2262px" width="14" height="22" aria-hidden="true"><path d="M3 2 L11 11 L3 20" fill="none" stroke="#fff" stroke-width="2.5"/></svg>

  <!-- contact -->
  <div class="abs map" role="img" aria-label="Street map showing the office location" style="background:linear-gradient(135deg,#eef0ec,#dfe3dc)"></div>
  <h2 class="title" style="left:463px;top:2440px"><span class="accent">GET</span> IN TOUCH</h2>
  <span class="rule" style="left:463px;top:2479px"></span>
  <span class="contact-label" style="left:469px;top:2514px">LOCATION</span>
  <p class="contact-value" style="left:469px;top:2534px">P.O. Box 40518<br>Brookhaven, Virginia 20199-0518</p>
  <span class="contact-label" style="left:659px;top:2514px">CONTACT US</span>
  <p class="contact-value dim" style="left:659px;top:2534px">Phone : +1 800 555 01 20</p>
  <p class="contact-value dim" style="left:659px;top:2566px">Email : hello@lanternfieldcollective.org</p>
  <span class="contact-label" style="left:469px;top:2626px">WORK HOURS</span>
  <p class="contact-value dim" style="left:469px;top:2646px">MON-FRI 09:00 – 19:00</p>
  <p class="contact-value dim" style="left:469px;top:2674px">SAT-SUN 10:00 – 14:00</p>
  <span class="contact-label" style="left:659px;top:2626px">FOLLOW US</span>
  <div class="social"><span></span><span></span><span></span><span></span></div>
</main>

<footer>
  <nav class="abs footer-nav"><span>HOME</span><span>WHO WE ARE</span><span>WHAT WE DO</span><span>BLOG</span><span>CONTACT US</span><span>DONATE</span></nav>
  <p class="abs copyright">Copyright © 2019 lanternfieldcollective | Powered by lanternfieldcollective Privacy &amp; Legal</p>
</footer>

</body>
</html>
```